Kestrel Bridge Consulting (KBC) Business Card Design

I would like to create double-sided business cards that contain:
1) Name: Derek Molvane
2) Phone Number: +1 (555) 218-4907
3) Email: Derek.Molvane@KestrelBridgeConsulting.example
4) Website: KestrelBridgeConsulting.example

I would like to include my logo and a color scheme similar to the Varnholt Grand Prix Ostera squad color scheme (black, silver, greenish-blue – but can also include regular blue)

What we do: Our company develops and delivers innovative and pragmatic information technology and cybersecurity risk and compliance solutions for organizations in the commercial market as well as the federal, and state/local sectors.

```html
<!DOCTYPE html>
<html lang="en">
<head>
<meta charset="utf-8">
<title>Kestrel Bridge Consulting — Business Card</title>
<link rel="stylesheet" href="https://fonts.googleapis.com/css2?family=Michroma&family=Lato:wght@400;700&display=swap">
<style>
  :root {
    --backdrop: #26282c;
    --card-deep: #0a1d4f;
    --card-mid: #0f2f73;
    --card-light: #1a4a9c;
    --accent: #2f9cf0;
    --accent-teal: #21c4c0;
    --text: #ffffff;
    --text-soft: #dfe8f7;
    --faint: rgba(120, 170, 240, 0.12);
  }
  * { box-sizing: border-box; margin: 0; padding: 0; }
  html, body {
    width: 1200px; height: 952px; overflow: hidden;
    background: var(--backdrop);
  }
  .sheet {
    width: 1200px; height: 952px;
    display: flex; align-items: center; justify-content: center; gap: 40px;
  }
  .card {
    position: relative;
    width: 540px; height: 309px;
    border-radius: 22px;
    overflow: hidden;
    background: radial-gradient(ellipse at 30% 25%, var(--card-light) 0%, var(--card-mid) 45%, var(--card-deep) 100%);
    box-shadow: 0 18px 40px rgba(0,0,0,0.5);
  }
  .card-texture {
    position: absolute; inset: 0;
    background: linear-gradient(160deg, rgba(60,130,220,0.10), rgba(10,30,80,0.0) 60%);
  }
  .brand {
    position: relative;
    display: flex; align-items: center; gap: 14px;
  }
  .brand-mark {
    border-radius: 50%;
    background: var(--accent);
    flex-shrink: 0;
  }
  .brand-divider {
    width: 1.5px; align-self: stretch;
    background: var(--text);
  }
  .brand-name {
    font-family: "Michroma", sans-serif;
    color: var(--text);
    text-transform: uppercase;
    line-height: 1.05;
    letter-spacing: 0.04em;
  }
  .faint-circle {
    position: absolute;
    border-radius: 50%;
    border: 22px solid var(--faint);
  }

  /* Front */
  .card-front { padding: 34px 38px; }
  .card-front .brand-mark { width: 58px; height: 58px; }
  .card-front .brand-name { font-size: 16px; }
  .card-front .faint-circle { width: 270px; height: 270px; right: -50px; bottom: -90px; }
  .holder-name {
    position: relative;
    margin-top: 28px;
    font-family: "Michroma", sans-serif;
    font-size: 21px;
    color: var(--text);
    letter-spacing: 0.03em;
    text-transform: uppercase;
  }
  .contact-list {
    position: relative;
    list-style: none;
    margin-top: 14px;
    display: flex; flex-direction: column; gap: 7px;
  }
  .contact-item {
    display: flex; align-items: center; gap: 9px;
    font-family: "Lato", sans-serif;
    font-size: 13px;
    color: var(--text-soft);
  }
  .contact-icon {
    width: 16px; height: 16px;
    border-radius: 3px;
    background: var(--accent-teal);
    display: flex; align-items: center; justify-content: center;
    flex-shrink: 0;
  }

  /* Back */
  .card-back { display: flex; align-items: center; justify-content: center; }
  .card-back .brand { gap: 18px; }
  .card-back .brand-mark { width: 84px; height: 84px; }
  .card-back .brand-name { font-size: 25px; }
  .card-back .faint-circle { width: 330px; height: 330px; left: 20px; top: -40px; }
</style>
</head>
<body>
<main class="sheet">
  <section class="card card-front" aria-label="Business card front">
    <div class="card-texture" role="img" aria-label="Soft blue background with a faint network-dot pattern"></div>
    <div class="faint-circle"></div>
    <div class="brand">
      <span class="brand-mark"></span>
      <span class="brand-divider"></span>
      <p class="brand-name">Kestrel<br>Bridge<br>Consulting</p>
    </div>
    <h1 class="holder-name">Derek Molvane</h1>
    <ul class="contact-list">
      <li class="contact-item">
        <span class="contact-icon">
          <svg width="10" height="10" viewBox="0 0 24 24" fill="#0a1d4f"><path d="M6.6 10.8a15.1 15.1 0 0 0 6.6 6.6l2.2-2.2c.3-.3.7-.4 1-.2 1.1.4 2.3.6 3.6.6.6 0 1 .4 1 1V20c0 .6-.4 1-1 1A17 17 0 0 1 3 4c0-.6.4-1 1-1h3.5c.6 0 1 .4 1 1 0 1.3.2 2.5.6 3.6.1.3 0 .7-.2 1z"/></svg>
        </span>
        +1 (555) 218-4907
      </li>
      <li class="contact-item">
        <span class="contact-icon">
          <svg width="10" height="10" viewBox="0 0 24 24" fill="none" stroke="#0a1d4f" stroke-width="2.5"><rect x="3" y="5" width="18" height="14" rx="1"/><path d="M3 6l9 7 9-7"/></svg>
        </span>
        Derek.Molvane@KestrelBridgeConsulting.example
      </li>
      <li class="contact-item">
        <span class="contact-icon">
          <svg width="10" height="10" viewBox="0 0 24 24" fill="none" stroke="#0a1d4f" stroke-width="2.5"><circle cx="12" cy="12" r="9"/><path d="M3 12h18M12 3c3 3 3 15 0 18M12 3c-3 3-3 15 0 18"/></svg>
        </span>
        KestrelBridgeConsulting.example
      </li>
    </ul>
  </section>

  <section class="card card-back" aria-label="Business card back">
    <div class="card-texture" role="img" aria-label="Soft blue background with a faint network-dot pattern"></div>
    <div class="faint-circle"></div>
    <div class="brand">
      <span class="brand-mark"></span>
      <span class="brand-divider"></span>
      <p class="brand-name">Kestrel<br>Bridge<br>Consulting</p>
    </div>
  </section>
</main>
</body>
</html>
```